Business Card *

A business card design
Use the logo uploaded in the brief page.
You may use placeholders in your design layouts.
I will provide the actual business card details to the winning designer.

Logo
Place for contact info (name, title, phone, email, etc)

Requirements
Must have
• Logo

```html
<!DOCTYPE html>
<html lang="en">
<head>
<meta charset="utf-8">
<title>Oakmere Agriculture and Industry – Business Card</title>
<link href="https://fonts.googleapis.com/css2?family=Roboto:wght@300;400;500;700&display=swap" rel="stylesheet">
<style>
  :root {
    --bg: #2e2f31;
    --green: #3cb44a;
    --green-light: #6cc56f;
    --grey: #8e9094;
    --grey-dark: #6d6e71;
    --white: #ffffff;
    --text-grey: #7a7c80;
  }
  * { box-sizing: border-box; margin: 0; padding: 0; }
  html, body { width: 1200px; height: 800px; overflow: hidden; }
  body {
    background: var(--bg);
    font-family: "Roboto", Arial, sans-serif;
    position: relative;
  }
  .card {
    position: absolute;
    width: 520px;
    height: 297px;
    overflow: hidden;
    box-shadow: 0 10px 30px rgba(0,0,0,.45);
  }
  /* Front */
  .card-front {
    left: 110px; top: 90px;
    background: radial-gradient(circle at 50% 52%, #a9acaa 0%, #8fb893 32%, #54b95c 62%, var(--green) 100%);
    display: flex; flex-direction: column; align-items: center; justify-content: center;
    color: var(--white);
  }
  .front-mark {
    width: 54px; height: 54px; border-radius: 50%;
    border: none; background: var(--white); margin-bottom: 14px;
  }
  .brand-name {
    font-weight: 700; font-size: 44px; letter-spacing: 1px; line-height: 1;
  }
  .brand-tagline {
    font-weight: 700; font-size: 12px; letter-spacing: 3px; text-transform: uppercase; margin-top: 6px;
  }
  .front-web { font-weight: 300; font-size: 14px; margin-top: 26px; letter-spacing: .5px; }

  /* Back */
  .card-back { left: 570px; top: 410px; background: var(--white); }
  .back-wave { position: absolute; left: 0; top: 0; width: 520px; height: 297px; }
  .back-logo {
    position: absolute; left: 50px; top: 70px; width: 210px;
    display: flex; flex-direction: column; align-items: center;
    color: var(--grey-dark);
  }
  .back-logo .front-mark { background: var(--grey-dark); width: 44px; height: 44px; margin-bottom: 10px; }
  .back-logo .brand-name { font-size: 34px; }
  .back-logo .brand-tagline { font-size: 9.5px; letter-spacing: 2px; }
  .divider {
    position: absolute; left: 278px; top: 48px; width: 1px; height: 120px; background: #c7c8ca;
  }
  .contact { position: absolute; left: 296px; top: 46px; }
  .person-name { color: var(--green); font-weight: 500; font-size: 21px; }
  .person-title { color: var(--text-grey); font-size: 13px; font-weight: 300; margin: 2px 0 12px; }
  .contact-line {
    display: flex; align-items: center; gap: 8px;
    color: var(--text-grey); font-size: 12.5px; font-weight: 300; margin-bottom: 5px;
  }
  .contact-line svg { width: 12px; height: 12px; flex: none; }
  .contact-line .accent { color: var(--green); }
  .address {
    position: absolute; right: 26px; bottom: 26px; text-align: right;
    color: var(--white); font-size: 13px; font-weight: 300; line-height: 1.3;
  }
</style>
</head>
<body>

<section class="card card-front">
  <div class="front-mark"></div>
  <div class="brand-name">OAKMERE</div>
  <div class="brand-tagline">Agriculture and Industry</div>
  <div class="front-web">www.oakmere-ag.com</div>
</section>

<section class="card card-back">
  <svg class="back-wave" viewBox="0 0 520 297" aria-hidden="true">
    <path d="M0,226 C180,236 340,200 482,138 C350,210 180,252 0,250 Z" fill="#9a9ca0"/>
    <path d="M0,262 C200,264 380,206 520,118 L520,297 L0,297 Z" fill="#3cb44a"/>
  </svg>

  <div class="back-logo">
    <div class="front-mark"></div>
    <div class="brand-name">OAKMERE</div>
    <div class="brand-tagline">Agriculture and Industry</div>
  </div>

  <div class="divider"></div>

  <div class="contact">
    <div class="person-name">Daniel Hartley</div>
    <div class="person-title">Manager</div>
    <div class="contact-line">
      <svg viewBox="0 0 24 24"><path fill="#3cb44a" d="M6.6 10.8a15 15 0 0 0 6.6 6.6l2.2-2.2c.3-.3.7-.4 1-.2 1.1.4 2.3.6 3.6.6.6 0 1 .4 1 1V20c0 .6-.4 1-1 1A17 17 0 0 1 3 4c0-.6.4-1 1-1h3.5c.6 0 1 .4 1 1 0 1.3.2 2.5.6 3.6.1.3 0 .7-.2 1z"/></svg>
      <span>555-010-2100</span>
    </div>
    <div class="contact-line">
      <svg viewBox="0 0 24 24" fill="none" stroke="#3cb44a" stroke-width="2"><rect x="3" y="5" width="18" height="14" rx="1"/><path d="M3 6l9 7 9-7"/></svg>
      <span>hello@oakmere-ag.com</span>
    </div>
    <div class="contact-line">
      <svg viewBox="0 0 24 24" fill="none" stroke="#3cb44a" stroke-width="2"><circle cx="12" cy="12" r="9"/><path d="M3 12h18M12 3c3 3 3 15 0 18M12 3c-3 3-3 15 0 18"/></svg>
      <span>www.<span class="accent">oakmere-ag</span>.com</span>
    </div>
  </div>

  <div class="address">Your address, city<br>state, ZIP 0000</div>
</section>

</body>
</html>
```